Design Labels and Brand Look For Mens Soap Company

We are developing a mens soap line for a natural body wash and exfoliating bar. We will be selling this with our line of mens toiletry bags that we sell under the name of Corvane Totes on Quillmart. We are looking for you to design the product brand look with brand color palette and fonts.

The title for the mens body was is "Body Wash For Men". The title for the soap bar is "Exfoliating Bar Soap For Men"

We are providing the templates for these 2 items in PDF form. The final version of the design needs to be in a layered PSD format. You also need to send us the fonts used.

This soap will be sold on Quillmart. Do a search for "men's body wash" and "mens soap bar" you will see our competition on page one. We need to stand out with colors and design differentiaon.

Target Market(s)

Men

Industry/Entity Type

Skin Care Product

Requirements
Must have
• Layered PSD file with all fonts

```html
<!DOCTYPE html>
<html lang="en">
<head>
<meta charset="utf-8">
<title>Corvane — Exfoliating Bar Soap For Men, Label</title>
<link rel="stylesheet" href="https://fonts.googleapis.com/css2?family=Cormorant+Garamond:wght@500;600&display=swap">
<style>
  :root {
    --backdrop: #c4c9d0;
    --carton-white: #f1f3f8;
    --lid-violet: #4a4289;
    --side-navy: #120f4b;
    --label-white: #ffffff;
    --label-gold: #d59a3e;
  }
  * { margin: 0; padding: 0; box-sizing: border-box; }
  html, body {
    width: 1200px; height: 800px; overflow: hidden;
    background: var(--backdrop);
  }
  .canvas {
    position: relative; width: 1200px; height: 800px;
    display: flex; align-items: center; justify-content: center;
  }
  .carton-net {
    display: grid;
    grid-template-columns: 120px 760px 120px;
    grid-template-rows: 430px 230px;
  }
  .end-flap { background: var(--carton-white); }
  .end-flap--lid { border-bottom: 1px solid #dfe2ea; }
  .panel {
    font-family: "Cormorant Garamond", Georgia, serif;
    font-weight: 500;
    text-transform: uppercase;
    line-height: 0.95;
  }
  .panel--lid {
    background: var(--lid-violet);
    display: flex; flex-direction: column; align-items: center; justify-content: center;
    gap: 36px;
  }
  .panel--side {
    background: var(--side-navy);
    display: flex; align-items: center; justify-content: center; gap: 70px;
  }
  .brand-name {
    font-family: "Cormorant Garamond", Georgia, serif;
    font-weight: 500;
    color: var(--label-gold);
    text-transform: none;
    letter-spacing: 0.02em;
  }
  .brand-name--lid { font-size: 64px; }
  .brand-name--side { font-size: 38px; }
  .product-title { text-align: center; letter-spacing: 0.04em; }
  .product-title--lid { font-size: 70px; }
  .product-title--side { font-size: 34px; text-align: left; }
  .product-title__line { display: block; color: var(--label-white); }
  .product-title__line--accent { color: var(--label-gold); }
</style>
</head>
<body>
<main class="canvas">
  <section class="carton-net" aria-label="Exfoliating bar soap carton label">
    <div class="end-flap end-flap--lid"></div>
    <div class="panel panel--lid">
      <span class="brand-name brand-name--lid">Corvane</span>
      <h1 class="panel product-title product-title--lid">
        <span class="product-title__line">Exfoliating</span>
        <span class="product-title__line">Bar Soap</span>
        <span class="product-title__line product-title__line--accent">For Men</span>
      </h1>
    </div>
    <div class="end-flap end-flap--lid"></div>

    <div class="end-flap"></div>
    <div class="panel panel--side">
      <span class="brand-name brand-name--side">Corvane</span>
      <h2 class="panel product-title product-title--side">
        <span class="product-title__line">Exfoliating</span>
        <span class="product-title__line">Bar Soap</span>
        <span class="product-title__line product-title__line--accent">For Men</span>
      </h2>
    </div>
    <div class="end-flap"></div>
  </section>
</main>
</body>
</html>
```